Poster design for the WILLOW WISP magic show.

We need a poster design for our magic show. This isn't your typical 'small town' magic show. Our show features world class magicians from the Velvet Lantern, in Hollywood California. The show is geared toward everyone, it is family friendly - with a little bit of an edge. We want people to see the poster and feel like they are going to have a unique and sophisticated magical experience. We also want individuals and couples to see the poster and feel like it is a show for them and not only for children.
Updates

Target Market(s)

BRT audience, family audience, the age range is anywhere from 5 - 105. Cool people.

Industry/Entity Type

Town

Requirements
Must have
• Our attached .jpg of the magician floating in the air. Poster size 24x36"
Must have text:
The 3rd Annual Albuquerque Conjuring Gala Presents (small type)
Willow Wisp (should be larger type)
November 24th - 25th
Showtimes 3:00PM & 7:30PM Saturday, 2:00PM Sunday
Tickets available at www.DorvaSeats.example For more information contact Dorva Theatre @ 505.555.0147
Nice to have
• A sort of old school/antique feeling to the poster.
Perhaps a theater marquee
Check out www.grovelumen.example - we love the feeling of this site for our poster...
Feel free to adjust the provided .jpg accordingly in regards to color/size/interaction with the rest of the poster
Should not have
• Should not have clowns, bunnies, anything that would make it feel like a 3 year old's magic themed birthday party.

```html
<!DOCTYPE html>
<html lang="en">
<head>
<meta charset="utf-8">
<title>Willow Wisp — Poster</title>
<link rel="stylesheet" href="https://fonts.googleapis.com/css2?family=Bebas+Neue&family=Limelight&display=swap">
<style>
  :root {
    --bg-deep: #1d0e0a;
    --bg-mid: #3a2118;
    --gold: #dcc56a;
    --cream: #f1ead8;
    --photo-dark: #2a1510;
    --photo-warm: #6b3a28;
  }
  * { margin: 0; padding: 0; box-sizing: border-box; }
  html, body { width: 806px; height: 1200px; overflow: hidden; background: var(--bg-deep); }
  .poster {
    position: relative;
    width: 806px;
    height: 1200px;
    background: radial-gradient(ellipse at 50% 35%, var(--bg-mid) 0%, #2a1610 55%, var(--bg-deep) 100%);
    font-family: "Bebas Neue", "Oswald", sans-serif;
    overflow: hidden;
  }
  .presenter {
    position: absolute; left: 32px; top: 44px;
    color: #e6dcc4; font-size: 31px; line-height: 35px; letter-spacing: 0.5px;
  }
  .presents {
    position: absolute; left: 214px; top: 46px; width: 28px; height: 108px;
  }
  .presents text { font-family: "Bebas Neue", sans-serif; font-size: 26px; fill: var(--gold); }
  .stars { position: absolute; color: var(--gold); font-size: 30px; letter-spacing: 8px; line-height: 1; }
  .stars--intro { left: 70px; top: 182px; }
  .date-month { position: absolute; left: 31px; top: 246px; font-size: 56px; color: var(--gold); line-height: 1; }
  .date-days { position: absolute; left: 31px; top: 309px; font-size: 56px; color: var(--cream); line-height: 1; }
  .date-days sup { font-size: 28px; vertical-align: 22px; }
  .title { position: absolute; left: 280px; top: 38px; width: 486px; height: 335px; }
  .title text { font-family: "Limelight", serif; fill: var(--cream); }
  .divider { position: absolute; left: 30px; width: 746px; height: 30px; }
  .divider--upper { top: 405px; }
  .divider--lower { top: 987px; }
  .showtimes { position: absolute; left: 30px; top: 478px; width: 206px; }
  .showtimes .label { display: block; line-height: 1; text-align: center; }
  .showtimes .gold { color: var(--gold); }
  .showtimes .time { color: var(--cream); }
  .st-heading { font-size: 48px; margin-top: 28px; }
  .st-time { font-size: 74px; margin-top: 2px; }
  .st-day { font-size: 54px; margin-top: 4px; }
  .st-day--big { font-size: 70px; margin-top: 2px; }
  .rule { width: 206px; height: 14px; display: block; }
  .feature-photo { position: absolute; left: 288px; top: 472px; width: 484px; height: 470px; }
  .photo-fill {
    position: absolute; left: 3px; top: 14px; width: 478px; height: 442px;
    background: radial-gradient(ellipse at 30% 20%, var(--photo-warm) 0%, #3d2016 45%, var(--photo-dark) 100%);
  }
  .photo-frame { position: absolute; inset: 0; }
  .footer {
    position: absolute; left: 0; top: 1046px; width: 806px; text-align: center;
    font-size: 32px; line-height: 38px; color: var(--gold); letter-spacing: 0.3px;
  }
  .footer .light { color: var(--cream); }
</style>
</head>
<body>
<main class="poster">
  <p class="presenter">THE 3RD ANNUAL<br>ALBUQUERQUE<br>CONJURING GALA</p>
  <svg class="presents" viewBox="0 0 28 108" aria-label="Presents">
    <text transform="translate(22 108) rotate(-90)" textLength="108" lengthAdjust="spacingAndGlyphs">PRESENTS</text>
  </svg>
  <div class="stars stars--intro">★★★</div>

  <p class="date-month">NOVEMBER</p>
  <p class="date-days">24<sup>TH</sup> - 25<sup>TH</sup></p>

  <svg class="title" viewBox="0 0 486 335" aria-label="Willow Wisp">
    <text x="4" y="142" font-size="150" textLength="478" lengthAdjust="spacingAndGlyphs">WILLOW</text>
    <text x="4" y="326" font-size="150" textLength="478" lengthAdjust="spacingAndGlyphs">WISP</text>
  </svg>

  <svg class="divider divider--upper" viewBox="0 0 746 30" aria-hidden="true">
    <g fill="#dcc56a">
      <path d="M0 15 L6 12 L6 18 Z"/><rect x="4" y="14" width="294" height="2"/><path d="M298 15 L292 12 L292 18 Z"/>
      <path d="M746 15 L740 12 L740 18 Z"/><rect x="446" y="14" width="296" height="2"/><path d="M446 15 L452 12 L452 18 Z"/>
      <text x="373" y="26" font-size="30" text-anchor="middle" letter-spacing="8" font-family="serif">★★★</text>
    </g>
  </svg>

  <section class="showtimes">
    <svg class="rule" viewBox="0 0 206 14" aria-hidden="true"><path d="M0 6 H86 Q96 6 103 1 Q110 6 120 6 H206 V8 H120 Q110 8 103 13 Q96 8 86 8 H0 Z" fill="#dcc56a"/></svg>
    <span class="label gold st-heading">SHOWTIMES</span>
    <span class="label time st-time">3:00PM</span>
    <span class="label time st-time">7:30PM</span>
    <span class="label gold st-day">SATURDAY</span>
    <span class="label time st-time">2:00PM</span>
    <span class="label gold st-day--big">SUNDAY</span>
    <svg class="rule" viewBox="0 0 206 14" aria-hidden="true" style="margin-top:22px"><path d="M0 6 H86 Q96 6 103 1 Q110 6 120 6 H206 V8 H120 Q110 8 103 13 Q96 8 86 8 H0 Z" fill="#dcc56a"/></svg>
  </section>

  <figure class="feature-photo">
    <div class="photo-fill" role="img" aria-label="Photo of the magician floating in mid-air beside a levitating chair on a dim stage"></div>
    <svg class="photo-frame" viewBox="0 0 484 470" aria-hidden="true">
      <rect x="2" y="14" width="480" height="442" fill="none" stroke="#dcc56a" stroke-width="3"/>
      <path d="M2 14 Q60 14 80 4 H404 Q424 14 482 14 V20 Q424 20 404 12 H80 Q60 20 2 20 Z" fill="#dcc56a"/>
      <path d="M2 456 Q60 456 80 466 H404 Q424 456 482 456 V450 Q424 450 404 458 H80 Q60 450 2 450 Z" fill="#dcc56a"/>
    </svg>
  </figure>

  <svg class="divider divider--lower" viewBox="0 0 746 30" aria-hidden="true">
    <g fill="#dcc56a">
      <path d="M0 15 L6 12 L6 18 Z"/><rect x="4" y="14" width="294" height="2"/><path d="M298 15 L292 12 L292 18 Z"/>
      <path d="M746 15 L740 12 L740 18 Z"/><rect x="446" y="14" width="296" height="2"/><path d="M446 15 L452 12 L452 18 Z"/>
      <text x="373" y="26" font-size="30" text-anchor="middle" letter-spacing="8" font-family="serif">★★★</text>
    </g>
  </svg>

  <footer class="footer">
    TICKETS AVAILABLE AT <span class="light">WWW.DORVASEATS.EXAMPLE</span><br>
    FOR MORE INFORMATION CONTACT <span class="light">DORVA THEATRE</span><br>
    <span class="light">@ 505.555.0147</span>
  </footer>
</main>
</body>
</html>
```